Online Art Gallery & Art Management Firm looking for a business card

I'm launching an online art gallery (paintings, photography, drawings, furniture, books, ...) where people can buy all types of art. It's a platform where young and unknown artists can showcase their oeuvre.

Additionally, the venture will act as my advising company for artists. I help them out with their business side of life and become their representative.

The company name: The Velmora House
Logo is attached

I'm looking for something very classy and upmarket.
Updates

Reason: Logo wasn't finished yet...

The design should include the following information: - Name: Pieter Drovensky - Title: Founder - Mobile: +32 (0) 485 613 204 - E-mail: pieter@velmora-house.net - Website www.velmora-house.net I prefer the have the logo (without website) on the one side and the information on the other. Best regards Pieter

Target Market(s)

Art buyers / art dealers / artists / middle class / upmarket /

Industry/Entity Type

Artists

Colors

Designer to choose colors to be used in the design.

Requirements
Must have
• Must communicate credibility, trust and integrity
Nice to have
• Something classy, chique
Should not have
• Nothing to artistic or creative

```html
<!DOCTYPE html>
<html lang="en">
<head>
<meta charset="UTF-8">
<title>The Velmora House — Business Card</title>
<link rel="stylesheet" href="https://fonts.googleapis.com/css2?family=Open+Sans:wght@300;400&display=swap">
<style>
  :root {
    --backdrop: #3a3534;
    --card-dark: #0b1111;
    --card-dark-glow: #161c1c;
    --card-light: #ffffff;
    --ink: #2a2a2a;
    --ink-soft: #555555;
    --logo-ink: #f4f4f4;
  }
  * { margin: 0; padding: 0; box-sizing: border-box; }
  html, body {
    width: 1200px;
    height: 1200px;
    overflow: hidden;
    background: var(--backdrop);
    font-family: "Open Sans", Arial, sans-serif;
  }
  .sheet {
    width: 1200px;
    height: 1200px;
    display: flex;
    flex-direction: column;
    align-items: center;
    justify-content: center;
    gap: 60px;
  }
  .card {
    position: relative;
    width: 860px;
    height: 500px;
    box-shadow: 0 14px 30px rgba(0, 0, 0, 0.35);
  }
  .card--front {
    background: radial-gradient(circle at 55% 45%, var(--card-dark-glow) 0%, var(--card-dark) 65%);
    display: flex;
    align-items: center;
    justify-content: center;
  }
  .wordmark {
    color: var(--logo-ink);
    font-weight: 300;
    font-size: 34px;
    letter-spacing: 0.24em;
    text-transform: uppercase;
  }
  .card--back {
    background: var(--card-light);
    color: var(--ink);
  }
  .logo-square {
    position: absolute;
    top: 44px;
    right: 62px;
    width: 156px;
    height: 156px;
    background: var(--card-dark);
    display: flex;
    align-items: flex-end;
    justify-content: center;
    padding-bottom: 14px;
  }
  .logo-square .wordmark {
    font-size: 9px;
    letter-spacing: 0.18em;
    white-space: nowrap;
  }
  .identity {
    position: absolute;
    left: 78px;
    top: 190px;
    font-weight: 300;
  }
  .identity__first {
    font-size: 54px;
    line-height: 1.05;
  }
  .identity__last {
    font-size: 38px;
    line-height: 1.15;
  }
  .identity__title {
    font-size: 22px;
    color: var(--ink-soft);
    margin-left: 6px;
  }
  .contact {
    position: absolute;
    left: 78px;
    top: 332px;
    display: grid;
    grid-template-columns: 66px auto;
    column-gap: 16px;
    row-gap: 2px;
    font-size: 16px;
    font-weight: 300;
    color: var(--ink-soft);
    line-height: 1.35;
  }
  .contact__label { text-align: right; }
  .contact__value { color: var(--ink); }
</style>
</head>
<body>
  <main class="sheet">
    <section class="card card--front" aria-label="Card front">
      <span class="wordmark">The Velmora House</span>
    </section>

    <section class="card card--back" aria-label="Card back">
      <div class="logo-square">
        <span class="wordmark">The Velmora House</span>
      </div>
      <div class="identity">
        <div class="identity__first">Pieter</div>
        <div class="identity__last">Drovensky<span class="identity__title">Founder</span></div>
      </div>
      <div class="contact">
        <span class="contact__label">Mobile</span>
        <span class="contact__value">+32 (0) 485 613 204</span>
        <span class="contact__label">Email</span>
        <span class="contact__value">pieter@velmora-house.net</span>
        <span class="contact__label"></span>
        <span class="contact__value">www.velmora-house.net</span>
      </div>
    </section>
  </main>
</body>
</html>
```